E@SY - Design a Few Web Pages for Website Mockup for Job Board & FORGET Tallowfern.com

Design a mockup site with just 5 simple pages (home, search results, job profile, employee and employer profile). Design can be whatever you prefer, HTML/CSS, Photoshop, etc.) for a new job board I am looking to create. Winner will most likely be the person who will help with building the actual site; unless winner chooses not to =(. The idea here is to NOT be the same as the other job boards Tallowfern.com, Brimquest.com, Workvantly.com, Kelp.com, which are dated. Looking for innovative simple features and nice designs that are easy to use and not complicated (i.e. site would render easily on mobile devices, slight transparency images, possibly fixed header bars - these are not what I'm asking for but just some examples of things that may liven up a website and make people want to come to the site and appreciate the design). Think Quillmosa, RoveNook, . Pages include:

1) Home Page / landing page - should only have a few fields and links and very appealing - different from tallowfern.com, workvantly.com, brimquest.com, etc. Search fields include "Keywords" and "Location". Links on the landing page should be "Sign in or Join", "Employers Post Jobs"

2) Job Search Results Page -Filter options should be:
a) Salary Range 30k+, 50k+, 80k+ 100k+
b) Distance: Exact Location, within 5, 10, 25, 50 miles
c) Company (i.e. all jobs for Zentrip)
d) Job Type (Part Time, Full Time, Internship, Contract / Temporary)

3) Candidate Profile Page (photo or avatar of Male or Female if no photo is provided)
a) Name
b) Location
c) Title
d) Education / School
e) Experience
f) ProVellum Profile link (if you want to have items a-e listed in the profile by pulling in from public ProVellum profile, that works too)

4) Job Profile Page
a) If Employer is logged in and looking at their own job page, they should be able to open / see a list of all candidates applying for this job with status options that employer can choose from (reject, consider, accept)
b) If job candidate is logged in and looking at the job page, they should be able to save the job, refer to a friend or apply

5) Employer Profile Page
a) Can post new jobs easily from here once they're logged in
b) list of # of jobs currently posted for this company with date posted and status (open, closed) and ability to click on any of the jobs to open up the job profile page

```html
<!DOCTYPE html>
<html lang="en">
<head>
<meta charset="utf-8">
<title>Jobs Tallowfern — Home</title>
<link href="https://fonts.googleapis.com/css2?family=Open+Sans:ital,wght@0,300;0,400;0,600;0,700;1,400&display=swap" rel="stylesheet">
<style>
:root{
  --purple:#8e44ad;
  --purple-deep:#7a3597;
  --purple-soft:#b488cc;
  --purple-bright:#cf9bf0;
  --purple-text:#9b4fbf;
  --ink:#3a3a3a;
  --ink-soft:#555;
  --tint:#f8f4fa;
  --tint-tab:#efe6f3;
  --white:#fff;
}
*{box-sizing:border-box;margin:0;padding:0}
html,body{width:1200px;height:3324px;overflow:hidden}
body{position:relative;font-family:'Open Sans',Arial,sans-serif;color:var(--ink);background:var(--white)}
.abs{position:absolute}

/* header */
.site-header{left:0;top:0;width:1200px;height:73px;background:var(--white)}
.brand{left:73px;top:20px;font-size:23px;color:var(--purple);font-weight:300;letter-spacing:.3px}
.brand b{font-weight:700}
.nav{position:absolute;right:279px;top:25px;display:flex;gap:28px}
.nav a{font-size:17px;color:var(--ink-soft);text-decoration:none;white-space:nowrap}
.nav a.active{color:var(--purple);font-weight:600}
.btn-post{left:959px;top:13px;width:168px;height:46px;background:var(--purple);color:var(--white);font-size:15px;display:flex;align-items:center;justify-content:center;border-radius:2px}

/* hero */
.hero{left:0;top:73px;width:1200px;height:738px;background:linear-gradient(100deg,#4d4a58 0%,#6f6d80 30%,#8f8c9f 55%,#7c706a 75%,#5e534d 100%)}
.hero-shade{left:0;top:73px;width:1200px;height:738px;background:radial-gradient(ellipse 520px 200px at 480px 400px,rgba(30,25,40,.45),rgba(30,25,40,0))}
.hero-title{left:164px;top:338px;font-size:46px;font-weight:300;color:var(--white);white-space:nowrap}
.hero-sub{left:164px;top:393px;font-size:22px;color:var(--white);white-space:nowrap;text-shadow:0 1px 3px rgba(0,0,0,.35)}
.hero-sub strong{font-weight:700}
.hero-sub em{font-style:normal;color:var(--purple-bright);font-weight:700}
.search-panel{left:151px;top:471px;width:870px;height:112px;background:rgba(235,232,240,.7)}
.field{top:484px;height:56px;background:var(--white);font-size:16px;color:#aaa;padding:16px 15px}
.btn-search{left:856px;top:484px;width:152px;height:56px;background:var(--purple);color:var(--white);font-weight:700;font-size:16px;display:flex;align-items:center;justify-content:center}
.adv-link{left:847px;top:553px;font-size:16px;color:var(--purple-deep);white-space:nowrap}
.slide-dots span{position:absolute;left:1139px;width:9px;height:9px;border-radius:50%;background:rgba(255,255,255,.8)}

/* sections */
.sec-title{font-size:22px;font-weight:600;color:var(--purple)}
.sec-title.dark{color:#222}
.sec-desc{font-size:16px;color:var(--ink-soft);white-space:nowrap}
.sec-rule{width:63px;height:2px;background:var(--purple-soft)}

.tab{top:1009px;height:54px;background:var(--tint-tab);font-size:17px;font-weight:600;color:#222;display:flex;align-items:center;justify-content:center}
.tab.current{background:var(--tint)}
.browse-panel{left:71px;top:1063px;width:1053px;height:368px;background:var(--tint)}
.cat-col{top:1085px;font-size:16.5px;line-height:33.3px;color:#444;list-style:none;white-space:nowrap}

.featured-band{left:0;top:1517px;width:1200px;height:530px;background:var(--tint)}
.company-card{top:1740px;width:243px;height:149px;background:var(--white);display:flex;align-items:center;justify-content:center;gap:10px;font-size:22px;font-weight:700;color:#1f3b5a}
.company-card i{display:block;width:22px;height:22px;background:#2a9fd6}
.pager{top:1917px;width:38px;height:38px;display:flex;align-items:center;justify-content:center}
.pager.prev{left:1049px;background:var(--purple)}
.pager.next{left:1089px;background:var(--purple-soft)}

.post-card{width:331px;height:221px;background:var(--tint)}
.post-photo{position:absolute;left:0;top:0;width:331px;height:148px}
.post-title{position:absolute;left:18px;top:163px;font-size:16.5px;font-weight:400;color:var(--purple-text);white-space:nowrap}
.post-meta{position:absolute;left:18px;top:187px;font-size:14.5px;font-style:italic;color:#444}

/* footer */
.site-footer{left:0;top:2797px;width:1200px;height:452px;background:var(--tint)}
.foot-brand{left:71px;top:2885px;font-size:23px;color:var(--purple);font-weight:300}
.foot-brand b{font-weight:700}
.foot-about{left:71px;top:2930px;width:245px;font-size:16.5px;line-height:28px;color:#333}
.foot-social-title{left:71px;top:3099px;font-size:16.5px;font-weight:700;color:var(--purple)}
.social i{position:absolute;top:3139px;width:24px;height:24px;background:var(--purple);border-radius:3px}
.foot-col{top:2885px}
.foot-col h4{font-size:16.5px;font-weight:700;color:var(--purple);margin-bottom:16px}
.foot-col ul{list-style:none;font-size:16.5px;line-height:28px;color:#333;white-space:nowrap}
.bottom-bar{left:0;top:3249px;width:1200px;height:75px;background:var(--purple);color:var(--white);font-size:15px}
.bottom-bar .copy{position:absolute;left:71px;top:26px}
.bottom-bar .legal{position:absolute;right:73px;top:26px}
</style>
</head>
<body>

<header class="abs site-header">
  <div class="abs brand">JOBS <b>TALLOWFERN</b></div>
  <nav class="nav">
    <a class="active">Home</a>
    <a>Submit Resume</a>
    <a>My Tallowfern</a>
    <a>Carreer Center</a>
    <a>Sign in</a>
  </nav>
  <div class="abs btn-post">Employers Post Jobs</div>
</header>

<section>
  <div class="abs hero" role="img" aria-label="Photo of a young man in glasses with headphones working on a laptop at an office desk"></div>
  <div class="abs hero-shade"></div>
  <h1 class="abs hero-title">Find a New Job.</h1>
  <p class="abs hero-sub">Job from employer in over <em>34,000</em> <strong>cities</strong> and <em>192</em> <strong>countries</strong>.</p>
  <div class="abs search-panel"></div>
  <div class="abs field" style="left:164px;width:332px">Keyword</div>
  <div class="abs field" style="left:509px;width:332px">Location</div>
  <div class="abs btn-search">SEARCH</div>
  <div class="abs adv-link">Advanced Job Search</div>
  <div class="slide-dots"><span style="top:383px"></span><span style="top:397px"></span><span style="top:411px"></span></div>
</section>

<section>
  <h2 class="abs sec-title" style="left:71px;top:898px">Borwse Jobs</h2>
  <p class="abs sec-desc" style="left:71px;top:933px">Vivamus auctor sapien vitae odio consectetur, sit amet accumsan lectus sagittis.</p>
  <div class="abs sec-rule" style="left:71px;top:972px"></div>
  <div class="abs tab current" style="left:71px;width:149px">Functions</div>
  <div class="abs tab" style="left:221px;width:147px">Industry</div>
  <div class="abs tab" style="left:369px;width:148px">Location</div>
  <div class="abs browse-panel"></div>
  <ul class="abs cat-col" style="left:97px">
    <li>Accounting (3643)</li><li>Admin &amp; HR (3295)</li><li>Banking / Finance (784)</li><li>Beauty Care / Health (334)</li><li>Building &amp; Construction (2422)</li><li>Design (1498)</li><li>Education (1262)</li><li>Engineering (4312)</li><li>Hospitality / F &amp; B (1776)</li><li>Information Technology (IT) (2702)</li>
  </ul>
  <ul class="abs cat-col" style="left:429px">
    <li>Insurance (140)</li><li>Management (145)</li><li>Manufacturing (1351)</li><li>Marketing / Public Relations (6804)</li><li>Media &amp; Advertising (604)</li><li>Medical Services (888)</li><li>Merchandising &amp; Purchasing (720)</li><li>Professional Services (638)</li><li>Property (275)</li><li>Public / Civil (137)</li>
  </ul>
  <ul class="abs cat-col" style="left:789px">
    <li>Sales / CS / Business Development (7300)</li><li>Sciences / Laboratory / R&amp;D (446)</li><li>Telecomm (93)</li><li>Transportation &amp; Logistics (1493)</li><li>Other (2000)</li>
  </ul>
</section>

<section>
  <div class="abs featured-band"></div>
  <h2 class="abs sec-title" style="left:73px;top:1618px">Featured Companies</h2>
  <p class="abs sec-desc" style="left:73px;top:1653px">Vivamus auctor sapien vitae odio consectetur, sit amet accumsan lectus sagittis.</p>
  <div class="abs sec-rule" style="left:73px;top:1692px"></div>
  <div class="abs company-card" style="left:73px"><i></i>Larkfield.com</div>
  <div class="abs company-card" style="left:343px"><i></i>Larkfield.com</div>
  <div class="abs company-card" style="left:612px"><i></i>Larkfield.com</div>
  <div class="abs company-card" style="left:881px"><i></i>Larkfield.com</div>
  <div class="abs pager prev"><svg width="14" height="18" viewBox="0 0 14 18"><path d="M10 2 L3 9 L10 16" fill="none" stroke="#fff" stroke-width="3"/></svg></div>
  <div class="abs pager next"><svg width="14" height="18" viewBox="0 0 14 18"><path d="M4 2 L11 9 L4 16" fill="none" stroke="#fff" stroke-width="3"/></svg></div>
</section>

<section>
  <h2 class="abs sec-title dark" style="left:73px;top:2133px">Recent Post</h2>
  <p class="abs sec-desc" style="left:73px;top:2167px">Vivamus auctor sapien vitae odio consectetur, sit amet accumsan lectus sagittis.</p>
  <div class="abs sec-rule" style="left:73px;top:2206px"></div>

  <article class="abs post-card" style="left:73px;top:2235px">
    <div class="post-photo" role="img" aria-label="Photo of a hand on a computer mouse" style="background:linear-gradient(180deg,#3e3a36,#8a8580 60%,#c9c6c2)"></div>
    <h3 class="post-title">Lorem ipsum dolor sit amet</h3><p class="post-meta">By Admin 14 April, 2014</p>
  </article>
  <article class="abs post-card" style="left:432px;top:2235px">
    <div class="post-photo" role="img" aria-label="Photo of someone writing in a notebook beside a potted plant" style="background:linear-gradient(160deg,#5b6a5c,#b7b9b2 50%,#6e6258)"></div>
    <h3 class="post-title">Lorem ipsum dolor sit amet</h3><p class="post-meta">By Admin 14 April, 2014</p>
  </article>
  <article class="abs post-card" style="left:792px;top:2235px">
    <div class="post-photo" role="img" aria-label="Photo of a woman reading her phone by a doorway" style="background:linear-gradient(90deg,#2d3b4a,#7c8793 45%,#b79a7c 70%,#c7c3bd)"></div>
    <h3 class="post-title">Lorem ipsum dolor sit amet</h3><p class="post-meta">By Admin 14 April, 2014</p>
  </article>
  <article class="abs post-card" style="left:73px;top:2484px">
    <div class="post-photo" role="img" aria-label="Photo of a person walking downstairs with a backpack" style="background:linear-gradient(90deg,#c9b49a,#5b4634 45%,#8a5a2c 70%,#6e3f1a)"></div>
    <h3 class="post-title">Lorem ipsum dolor sit amet</h3><p class="post-meta">By Admin 14 April, 2014</p>
  </article>
  <article class="abs post-card" style="left:432px;top:2484px">
    <div class="post-photo" role="img" aria-label="Blurred photo of people in an office" style="background:linear-gradient(180deg,#d6d8dc,#9aa3ad 55%,#4c6580)"></div>
    <h3 class="post-title">Lorem ipsum dolor sit amet</h3><p class="post-meta">By Admin 14 April, 2014</p>
  </article>
  <article class="abs post-card" style="left:792px;top:2484px">
    <div class="post-photo" role="img" aria-label="Photo of a plant and laptop on a desk" style="background:linear-gradient(90deg,#4c5a3a,#c9c9c6 40%,#e6e6e4)"></div>
    <h3 class="post-title">Lorem ipsum dolor sit amet</h3><p class="post-meta">By Admin 14 April, 2014</p>
  </article>
</section>

<footer>
  <div class="abs site-footer"></div>
  <div class="abs foot-brand">JOB <b>TALLOWFERN</b></div>
  <p class="abs foot-about">Lorem ipsum dolor sit amet, consectetur adipiscing elit. Morbi in fringilla purus. Morbi et elit ac sem venenatis luctus ut eu massa.</p>
  <div class="abs foot-social-title">OUR SOCIAL</div>
  <div class="social"><i style="left:71px"></i><i style="left:100px"></i><i style="left:130px"></i><i style="left:162px"></i></div>
  <div class="abs foot-col" style="left:432px"><h4>Job Seekers</h4><ul><li>Search Jobs</li><li>Post Resumes</li><li>Job Alerts</li><li>Get Jobs in Email</li><li>My Job Tallowfern</li><li>Help</li></ul></div>
  <div class="abs foot-col" style="left:612px"><h4>Employer</h4><ul><li>Post a Job</li><li>Search Candidates</li><li>Advertise with Us</li></ul></div>
  <div class="abs foot-col" style="left:792px"><h4>About Us</h4><ul><li>About Job Tallowfern</li><li>FAQ</li><li>Be Safe</li><li>Fraud/Security</li><li>Report a Bug/Abuse</li><li>Career Job Tallowfern</li><li>Contact Us</li><li>Sitemap</li></ul></div>
  <div class="abs foot-col" style="left:979px"><h4>Tools</h4><ul><li>Tallowfern on Mobile</li><li>Customer Speaks</li><li>RSS</li><li>Widget to Your Site</li></ul></div>
  <div class="abs bottom-bar">
    <span class="copy">Copyright © 2014 Job Tallowfern.</span>
    <span class="legal">Privacy Policy &nbsp;|&nbsp; Terms and Conditions</span>
  </div>
</footer>

</body>
</html>
```